This is for a poster that will be hanging in the window of a Men's Suit Store in the mall:
Size 4 feet wide by 6 feet high
Main point is: A sale on "Suits" or "Men's Suits" at 40%-60% off ( the 40%-60% off should be the focal point)
Some words that can be used are "Sale" or "Clearance Sale"
Some key words that can be used to make it urgent are "limited time offer" or something similar.
You can get creative, the point is for the customer to want to come into the store and buy a suit right away.
You may use a graphic (picture of a man in a suit). It is not necessary but if it looks good you can use it. (If you do use a picture, it should be of a modern fit or slim fit suit)
Sorry, the initial brief somehow got deleted from the project. Please see the updated brief.
Thanks
Reason: Project was closed for some reason, extended to give enough time to complete
Mostly Men ages 35-55
Store
Designer to choose colors to be used in the design.

```html
<!DOCTYPE html>
<html lang="en">
<head>
<meta charset="utf-8">
<title>Clearance Sale Poster</title>
<link rel="stylesheet" href="https://fonts.googleapis.com/css2?family=Anton&family=Josefin+Sans:wght@400;600&display=swap">
<style>
  :root {
    --red-deep: #8a1608;
    --red-mid: #a8220f;
    --red-warm: #c0452a;
    --red-shadow: #4a0803;
    --white: #ffffff;
    --off-white: #f4f4f4;
    --band-grey: #9a9a9a;
    --footer-light: #c05a3e;
    --footer-dark: #a52a17;
  }
  html, body {
    margin: 0;
    padding: 0;
    width: 800px;
    height: 1200px;
    overflow: hidden;
    background: var(--red-mid);
  }
  .poster {
    position: relative;
    width: 800px;
    height: 1200px;
    overflow: hidden;
  }
  .poster svg {
    position: absolute;
    left: 0;
    top: 0;
    display: block;
  }
  .headline-figures { font-family: "Anton", "Oswald", sans-serif; }
  .headline-light { font-family: "Josefin Sans", "Montserrat", sans-serif; font-weight: 400; }
  .footer-offer { font-family: "Josefin Sans", "Montserrat", sans-serif; font-weight: 600; }
</style>
</head>
<body>
<main class="poster">
  <svg class="poster-background" width="800" height="1200" viewBox="0 0 800 1200" aria-hidden="true">
    <defs>
      <linearGradient id="bgGradient" x1="0" y1="0" x2="1" y2="1">
        <stop offset="0" stop-color="var(--red-mid)"/>
        <stop offset="0.45" stop-color="var(--red-deep)"/>
        <stop offset="1" stop-color="var(--red-warm)"/>
      </linearGradient>
    </defs>
    <rect width="800" height="1200" fill="url(#bgGradient)"/>
  </svg>

  <svg class="model-photo" width="800" height="1200" viewBox="0 0 800 1200" role="img" aria-label="Photo of a man in a slim fit dark suit, tinted red">
    <defs>
      <radialGradient id="suitTone" cx="0.5" cy="0.5" r="0.5">
        <stop offset="0" stop-color="#6e0e05" stop-opacity="0.75"/>
        <stop offset="1" stop-color="#6e0e05" stop-opacity="0"/>
      </radialGradient>
    </defs>
    <ellipse cx="400" cy="520" rx="380" ry="560" fill="url(#suitTone)"/>
  </svg>

  <svg class="poster-type" width="800" height="1200" viewBox="0 0 800 1200">
    <defs>
      <linearGradient id="bandGradient" x1="0" y1="0" x2="0" y2="1">
        <stop offset="0" stop-color="var(--white)"/>
        <stop offset="0.45" stop-color="var(--off-white)"/>
        <stop offset="1" stop-color="var(--band-grey)"/>
      </linearGradient>
      <linearGradient id="footerGradient" x1="0" y1="0" x2="1" y2="0">
        <stop offset="0" stop-color="var(--footer-light)"/>
        <stop offset="1" stop-color="var(--footer-dark)"/>
      </linearGradient>
      <linearGradient id="bandShade" x1="0" y1="0" x2="0" y2="1">
        <stop offset="0" stop-color="#000" stop-opacity="0"/>
        <stop offset="1" stop-color="#000" stop-opacity="0.45"/>
      </linearGradient>
    </defs>

    <g class="discount">
      <text class="headline-figures" x="47" y="284" font-size="265" textLength="574" lengthAdjust="spacingAndGlyphs" fill="var(--red-shadow)">40-60%</text>
      <text class="headline-figures" x="43" y="280" font-size="265" textLength="574" lengthAdjust="spacingAndGlyphs" fill="var(--off-white)">40-60%</text>
      <g transform="translate(760 280) rotate(-90)">
        <text class="headline-figures" x="-4" y="4" font-size="163" textLength="217" lengthAdjust="spacingAndGlyphs" fill="var(--red-shadow)">OFF</text>
        <text class="headline-figures" x="0" y="0" font-size="163" textLength="217" lengthAdjust="spacingAndGlyphs" fill="var(--off-white)">OFF</text>
      </g>
    </g>

    <text class="headline-light" x="46" y="421" font-size="117" textLength="717" lengthAdjust="spacingAndGlyphs" fill="var(--white)">CLEARANCE</text>

    <g class="sale-word">
      <text class="headline-figures" x="39" y="950" font-size="578" textLength="734" lengthAdjust="spacingAndGlyphs" fill="var(--red-shadow)">SALE</text>
      <text class="headline-figures" x="34" y="945" font-size="578" textLength="734" lengthAdjust="spacingAndGlyphs" fill="var(--white)">SALE</text>
    </g>

    <polygon class="band-shadow" points="0,930 800,870 800,943 0,1006" fill="url(#bandShade)"/>
    <polygon class="divider-band" points="0,1006 800,943 800,1057 0,1057" fill="url(#bandGradient)"/>

    <rect class="footer" x="0" y="1057" width="800" height="143" fill="url(#footerGradient)"/>
    <rect x="0" y="1057" width="800" height="6" fill="#000" opacity="0.25"/>
    <text class="footer-offer" x="55" y="1160" font-size="71" textLength="699" lengthAdjust="spacingAndGlyphs" fill="var(--white)">Limited Time Offer</text>
  </svg>
</main>
</body>
</html>
```